Lantern Trellis Advertisement

I need a great graphic to advertise for a program we have developed for older married couples. I would like it to help "sell" couples to join us for these events. Want to be able to add information like date(s), times, etc. when advertising a specific date and location. Could include picture(s) of age-appropriate couple(s). Would like it to fill 5.5 x 8.5 and have a bit of the 60's-70's feel. I am attaching a flyer that was created but am not happy with how it looks now. You can take any thing from it those to help with your design.
Target Market(s)
Married Couples born from 1940's through 1960's that would be considered Baby Boomers.
Colors
Designer to choose colors to be used in the design.
Requirements
Must have
- No need for dates, locations, etc. as we can print that information on the back.
Nice to have
- Eye catching to this generation but not cutesy Not too busy.

```html
<!DOCTYPE html>
<html lang="en">
<head>
<meta charset="utf-8">
<title>Lantern Trellis – A Day of Reflection</title>
<link rel="stylesheet" href="https://fonts.googleapis.com/css2?family=Montserrat:wght@800&family=PT+Sans+Narrow:wght@400;700&display=swap">
<style>
  :root {
    --navy: #0f4a73;
    --panel: #e4e4e4;
    --white: #fafafa;
    --gold: #d2c796;
    --green: #5f9a2e;
    --green-light: #8cc63f;
    --lime: #7ab648;
    --ink: #1d1d1d;
    --backdrop: #454545;
  }
  html, body {
    margin: 0;
    width: 1200px;
    height: 1200px;
    overflow: hidden;
    background: var(--backdrop);
  }
  .flyer {
    position: absolute;
    left: 231px;
    top: 30px;
    width: 738px;
    height: 1140px;
  }
  .flyer svg { display: block; }
  .headline {
    font-family: "Montserrat", sans-serif;
    font-weight: 800;
    fill: var(--white);
  }
  .brand-name {
    font-family: "PT Sans Narrow", sans-serif;
    font-weight: 700;
    fill: var(--navy);
    letter-spacing: 4px;
  }
  .tagline {
    font-family: "PT Sans Narrow", sans-serif;
    font-weight: 400;
    fill: var(--ink);
  }
  .audience {
    font-family: "PT Sans Narrow", sans-serif;
    font-weight: 700;
    fill: var(--navy);
  }
  .years {
    font-family: "PT Sans Narrow", sans-serif;
    font-weight: 700;
    fill: var(--lime);
  }
</style>
</head>
<body>
<div class="flyer">
  <svg width="738" height="1140" viewBox="0 0 738 1140" xmlns="http://www.w3.org/2000/svg">
    <defs>
      <linearGradient id="ribbon-fill" x1="0" y1="0" x2="1" y2="0">
        <stop offset="0" stop-color="#4f8a26"/>
        <stop offset="0.5" stop-color="#8cc63f"/>
        <stop offset="1" stop-color="#4f8a26"/>
      </linearGradient>
      <radialGradient id="photo-fill" cx="0.5" cy="0.45" r="0.6">
        <stop offset="0" stop-color="#e9dcc0"/>
        <stop offset="0.55" stop-color="#d9b64a"/>
        <stop offset="1" stop-color="#b6a24a"/>
      </radialGradient>
      <linearGradient id="emblem-fill" x1="0" y1="0" x2="0" y2="1">
        <stop offset="0" stop-color="#b9d99a"/>
        <stop offset="1" stop-color="#c9d3dc"/>
      </linearGradient>
      <polygon id="burst-spike" points="0,-250 -19,-208 19,-208"/>
    </defs>

    <!-- frame -->
    <rect class="frame-outer" x="0" y="0" width="738" height="1140" fill="var(--navy)"/>
    <rect class="frame-line" x="33" y="33" width="672" height="1074" fill="none" stroke="var(--white)" stroke-width="5"/>
    <rect class="frame-panel" x="55" y="55" width="628" height="1030" fill="var(--panel)"/>
    <rect class="frame-line-inner" x="55" y="55" width="628" height="1030" fill="none" stroke="var(--white)" stroke-width="4"/>
    <g class="frame-corners" fill="var(--white)">
      <rect x="28" y="28" width="30" height="30"/>
      <rect x="680" y="28" width="30" height="30"/>
      <rect x="28" y="1082" width="30" height="30"/>
      <rect x="680" y="1082" width="30" height="30"/>
    </g>

    <!-- badge -->
    <g class="badge-burst" transform="translate(366 300)" fill="var(--navy)">
      <circle r="214"/>
      <use href="#burst-spike" transform="rotate(0)"/><use href="#burst-spike" transform="rotate(10)"/>
      <use href="#burst-spike" transform="rotate(20)"/><use href="#burst-spike" transform="rotate(30)"/>
      <use href="#burst-spike" transform="rotate(40)"/><use href="#burst-spike" transform="rotate(50)"/>
      <use href="#burst-spike" transform="rotate(60)"/><use href="#burst-spike" transform="rotate(70)"/>
      <use href="#burst-spike" transform="rotate(80)"/><use href="#burst-spike" transform="rotate(90)"/>
      <use href="#burst-spike" transform="rotate(100)"/><use href="#burst-spike" transform="rotate(110)"/>
      <use href="#burst-spike" transform="rotate(120)"/><use href="#burst-spike" transform="rotate(130)"/>
      <use href="#burst-spike" transform="rotate(140)"/><use href="#burst-spike" transform="rotate(150)"/>
      <use href="#burst-spike" transform="rotate(160)"/><use href="#burst-spike" transform="rotate(170)"/>
      <use href="#burst-spike" transform="rotate(180)"/><use href="#burst-spike" transform="rotate(190)"/>
      <use href="#burst-spike" transform="rotate(200)"/><use href="#burst-spike" transform="rotate(210)"/>
      <use href="#burst-spike" transform="rotate(220)"/><use href="#burst-spike" transform="rotate(230)"/>
      <use href="#burst-spike" transform="rotate(240)"/><use href="#burst-spike" transform="rotate(250)"/>
      <use href="#burst-spike" transform="rotate(260)"/><use href="#burst-spike" transform="rotate(270)"/>
      <use href="#burst-spike" transform="rotate(280)"/><use href="#burst-spike" transform="rotate(290)"/>
      <use href="#burst-spike" transform="rotate(300)"/><use href="#burst-spike" transform="rotate(310)"/>
      <use href="#burst-spike" transform="rotate(320)"/><use href="#burst-spike" transform="rotate(330)"/>
      <use href="#burst-spike" transform="rotate(340)"/><use href="#burst-spike" transform="rotate(350)"/>
      <circle class="badge-ring" r="206" fill="var(--gold)"/>
      <circle class="badge-photo" r="197" fill="url(#photo-fill)" role="img" aria-label="Photo of a smiling older couple embracing outdoors in front of autumn foliage"/>
    </g>

    <!-- ribbon -->
    <g class="ribbon">
      <polygon class="ribbon-tail" points="55,436 150,436 150,522 72,522 100,479" fill="var(--green-light)"/>
      <polygon class="ribbon-tail" points="683,436 588,436 588,522 666,522 638,479" fill="var(--green-light)"/>
      <rect class="ribbon-band" x="118" y="419" width="500" height="85" fill="url(#ribbon-fill)"/>
      <text class="headline" x="368" y="476" text-anchor="middle" font-size="36" textLength="450" lengthAdjust="spacingAndGlyphs">A DAY OF REFLECTION</text>
    </g>

    <!-- brand -->
    <text class="brand-name" x="369" y="690" text-anchor="middle" font-size="52">LANTERN TRELLIS</text>
    <rect class="brand-emblem" x="175" y="712" width="390" height="190" rx="14" fill="url(#emblem-fill)" role="img" aria-label="Decorative artwork: green floral garland above a dove outline surrounded by a word cloud of marriage and faith words"/>

    <!-- message -->
    <text class="tagline" x="369" y="950" text-anchor="middle" font-size="28">Building a Vibrant Generation of Catholic</text>
    <text class="audience" x="369" y="1000" text-anchor="middle" font-size="42">COUPLES BORN FROM</text>
    <text class="years" x="369" y="1046" text-anchor="middle" font-size="40">1946 - 1964!</text>
  </svg>
</div>
</body>
</html>
```